FACIAL COSMETICS BUSINESS CARD

WE ARE A DENTAL PRACTICE BUT ARE OPENING UP A BRANCH FOR FACILA COSMETICS, LIKE BOTOX, FILLERS, PEELS, ETC. MAEVE AND ISOLDA WILL BE RUNNING THAT PART OF THE BUSINESS.
OUR CURRENT CARD IS ATTACHED AND OUR LOGO IT ATTACHED TOO. THE LOGO HAS ON IT OVEN DENTAL, I WOULD LIKE IT TO SAY OVEN COSMETICS, THE PHONE NUMBERS ON IT HAS TO BE REPLACED BY THE ONES I GAVE PREVIOUSLY AND THE WEB ADDRESS HAS TO BE DELETED, THE OTHER SIDE OF THE CARD HAS A MAP WHICH HAS TO BE DELETED, ADD TWO DATE-TIME LINES, I LIKE THE CARDS TO BE SIMPLE AND CLEAN, SIZE HAS TO BE NO LARGER THAN 5CMx8.5CM.
THE CARD HAS TO BE MATTE, I HATE GLOSSY, ABLE TO BE WRITTEN ON BOTH SIDES

Updates
I HAVE ATTACHED THE FILES, THEY CONSIST OF OUR CURRENT LOGO IN A FEW FORMS AND OUR BUSINESS CARD FOR THE DENTAL BRANCH, PLEASE COPY THE CURRENT DESIGN BUT ADDING THE REQUESTED CHANGES

Industry/Entity Type
Business
Contact Information for Business Card
OVEN COSMETICS
MAEVE : 0438 572 913
ISOLDA : 0429 638 207
SUITE 8 COLWOOD PARK ARCADE
74-86 HALBERT STREET
COLWOOD PARK NSW 2284
Logo Text
OVEN COSMETICS
Look and feel

```html
<!DOCTYPE html>
<html lang="en">
<head>
<meta charset="utf-8">
<title>Appointment Card — Back</title>
<link rel="stylesheet" href="https://fonts.googleapis.com/css2?family=Roboto+Condensed:wght@700&display=swap">
<style>
  :root {
    --page-bg: #ffffff;
    --card-bg: #ffffff;
    --card-border: #4a4a4a;
    --label-ink: #231f20;
    --rule-green: #5dbb3a;
  }
  html, body {
    margin: 0;
    padding: 0;
    width: 1200px;
    height: 1000px;
    overflow: hidden;
    background: var(--page-bg);
  }
  .card-back {
    position: absolute;
    left: 172px;
    top: 248px;
    width: 854px;
    height: 501px;
    background: var(--card-bg);
    border: 1px solid var(--card-border);
  }
  .field-label {
    position: absolute;
    left: 243px;
    margin: 0;
    font-family: "Roboto Condensed", "Arial Narrow", sans-serif;
    font-weight: 700;
    font-size: 34px;
    line-height: 34px;
    letter-spacing: -0.8px;
    color: var(--label-ink);
    white-space: nowrap;
  }
  .field-label--date { top: 189px; }
  .field-label--time { top: 256px; }
  .field-rule {
    position: absolute;
    left: 331px;
    width: 259px;
    height: 4px;
    background-image: linear-gradient(to right, var(--rule-green) 0 3.6px, transparent 3.6px 100%);
    background-size: 6.5px 4px;
    background-repeat: repeat-x;
  }
  .field-rule--date { top: 211px; }
  .field-rule--time { top: 278px; }
</style>
</head>
<body>
  <section class="card-back" aria-label="Appointment card back">
    <p class="field-label field-label--date">DATE:</p>
    <span class="field-rule field-rule--date" aria-hidden="true"></span>
    <p class="field-label field-label--time">TIME:</p>
    <span class="field-rule field-rule--time" aria-hidden="true"></span>
  </section>
</body>
</html>
```